BQN Project Signage

Need a sign to be displayed in the front of properties currently under Construction or Renovation to advertise our company information. Need it to be Professional and Contemporary. We are a Design/Build Construction Company. Information should include Company Name, email, website, phone number. Attached: Logo and company brochure, also included and inspiration images

```html
<!DOCTYPE html>
<html lang="en">
<head>
<meta charset="utf-8">
<title>BQN Construction – Project Sign</title>
<link rel="stylesheet" href="https://fonts.googleapis.com/css2?family=Bebas+Neue&family=Montserrat:wght@500&family=Oswald:wght@500&display=swap">
<style>
  :root {
    --backdrop: #e7e7e4;
    --sign-white: #ffffff;
    --charcoal: #333333;
    --lime: #e9e84a;
  }
  html, body {
    margin: 0;
    width: 1200px;
    height: 942px;
    overflow: hidden;
    background: var(--backdrop);
  }
  .canvas {
    position: relative;
    width: 1200px;
    height: 942px;
  }
  .sign {
    position: absolute;
    left: 286px;
    top: 0;
    width: 628px;
    height: 942px;
    background: var(--sign-white);
    overflow: hidden;
  }
  .sign-shapes {
    position: absolute;
    inset: 0;
  }
  .brand {
    position: absolute;
    left: 0;
    right: 0;
    top: 230px;
    text-align: center;
    color: var(--charcoal);
  }
  .brand-name {
    margin: 0;
    font-family: "Oswald", sans-serif;
    font-weight: 500;
    font-size: 56px;
    letter-spacing: 3px;
    line-height: 1;
  }
  .brand-rule {
    width: 540px;
    height: 4px;
    margin: 12px auto 10px;
    background: var(--lime);
  }
  .brand-tagline {
    margin: 0;
    font-family: "Oswald", sans-serif;
    font-weight: 500;
    font-size: 26px;
    letter-spacing: 3px;
  }
  .contact-title,
  .contact-web,
  .office-line,
  .main-phone,
  .address {
    position: absolute;
    left: 0;
    right: 0;
    margin: 0;
    text-align: center;
    white-space: nowrap;
  }
  .contact-title {
    top: 494px;
    height: 104px;
    line-height: 104px;
    font-family: "Bebas Neue", sans-serif;
    font-weight: 400;
    font-size: 116px;
    color: var(--charcoal);
  }
  .contact-title span {
    display: inline-block;
    letter-spacing: 1px;
    transform: scaleX(1.12);
  }
  .contact-web {
    top: 603px;
    line-height: 24px;
    font-family: "Bebas Neue", sans-serif;
    font-size: 22px;
    letter-spacing: 1.4px;
    color: var(--charcoal);
  }
  .office-line {
    top: 642px;
    line-height: 1;
    font-family: "Bebas Neue", sans-serif;
    font-size: 76px;
    letter-spacing: 1px;
    color: var(--sign-white);
  }
  .main-phone {
    top: 718px;
    height: 120px;
    line-height: 124px;
    font-family: "Bebas Neue", sans-serif;
    font-size: 114px;
    color: var(--charcoal);
  }
  .main-phone span {
    display: inline-block;
    transform: scaleY(1.22);
  }
  .address {
    top: 854px;
    font-family: "Montserrat", sans-serif;
    font-weight: 500;
    font-size: 19px;
    color: var(--sign-white);
  }
</style>
</head>
<body>
<main class="canvas">
  <section class="sign">
    <svg class="sign-shapes" width="628" height="942" viewBox="0 0 628 942" aria-hidden="true">
      <polygon points="0,0 170,0 415,105 0,198" fill="var(--lime)"/>
      <polygon points="170,0 628,0 628,205 415,105" fill="var(--charcoal)"/>
      <rect x="0" y="525" width="628" height="417" fill="var(--charcoal)"/>
      <polygon points="40,502 52,486 574,486 586,502" fill="var(--lime)"/>
      <rect x="40" y="500" width="546" height="132" fill="var(--lime)"/>
      <rect x="40" y="718" width="546" height="120" rx="14" fill="var(--lime)"/>
    </svg>

    <header class="brand">
      <h1 class="brand-name">BQN CONSTRUCTION</h1>
      <div class="brand-rule"></div>
      <p class="brand-tagline">LUXURY RENOVATIONS</p>
    </header>

    <h2 class="contact-title"><span>CONTACT US!</span></h2>
    <p class="contact-web">MARCO@BQNCONSTRUCTION.COM | WWW.BQNCONSTRUCTION.COM</p>
    <p class="office-line">OFFICE – 555.010.2468</p>
    <p class="main-phone"><span>555.010.7731</span></p>
    <p class="address">1450 Harbor View Rd., Ste. 118. Coral Point, FL 33000</p>
  </section>
</main>
</body>
</html>
```